Cyber security consulting company need a redesign web site

We need a new stylish and slick web design for our Cyber security company (our old https://vultrimadvisory.com)
Tolvane Consulting is comprised of a dedicated team of security experts who each have a wide range of expertise and experience in all areas of information security and Cyber such as APT (Advanced persistent threat ) test, penetration test, professional services, Standard & regulation Audit (e.g. ISO27001/2 , PCI DSS, WLA) and security assessment

We are looking for single page application (architecture) base on WordPress platform which brings our potential customer overwhelming experience and simple navigation within our new site.

Attached high level design document

Industry/Entity Type

It Company

Coding

Coded - Design and coding required

Font styles to use
Sans Serif

Colors
0255a3
0492cd
3276b5

Requirements
Must have
• The project must include all web element (HTML & CSS, JavaScript etc..) to be install on WordPress without any special requirement (best practices package or add-on package are acceptable)

```html
<!DOCTYPE html>
<html lang="en">
<head>
<meta charset="utf-8">
<title>Tolvane Consulting</title>
<link href="https://fonts.googleapis.com/css2?family=Poppins:wght@300;400;500;600&display=swap" rel="stylesheet">
<style>
:root{
  --blue:#3276b5;
  --blue-deep:#0255a3;
  --blue-bright:#0492cd;
  --slate:#3a4a55;
  --light:#f5f6f8;
  --ink:#2b2f36;
  --muted:#6a6f76;
  --footer:#2a2d36;
  --footer-deep:#22252c;
  --white:#ffffff;
  --field:#33363f;
}
*{box-sizing:border-box;margin:0;padding:0}
html,body{width:1200px;height:3232px;overflow:hidden}
body{font-family:'Poppins',sans-serif;color:var(--ink);background:var(--white);position:relative}
.page{position:relative;width:1200px;height:3232px}
section,header,footer{position:absolute;left:0;width:1200px}
.hero{top:0;height:711px;background:linear-gradient(135deg,#8fb6c9 0%,#e8ecef 35%,#f4f5f6 55%,#a7c2d1 80%,#4a6a84 100%)}
.site-header{top:0;left:65px;width:1065px;height:70px;background:var(--white);display:flex;align-items:center;padding:0 30px;box-shadow:0 2px 6px rgba(0,0,0,.08);z-index:2}
.brand{display:flex;align-items:center;gap:10px;font-weight:600;font-size:28px;color:var(--blue);letter-spacing:1px}
.brand-dot{width:28px;height:28px;border-radius:50%;background:var(--blue)}
.nav{margin-left:auto;margin-right:260px;display:flex;gap:34px;font-size:12px;font-weight:500;color:var(--ink)}
.section-title{font-weight:600;font-size:20px;text-align:center;text-transform:uppercase}
.about{top:711px;height:291px;background:var(--slate);color:var(--white)}
.about .section-title{position:absolute;top:60px;width:100%}
.about-text{position:absolute;left:246px;top:108px;width:600px;font-size:11px;line-height:21px;font-weight:300}
.btn{display:inline-block;background:var(--blue);color:var(--white);font-size:10px;font-weight:600;text-transform:uppercase;border-radius:3px}
.about .btn{position:absolute;left:883px;top:131px;width:104px;height:37px;line-height:37px;text-align:center}
.services{top:1002px;height:672px;background:var(--light)}
.services .section-title{position:absolute;top:62px;width:100%}
.card{position:absolute;width:239px;height:229px;background:var(--white);box-shadow:0 1px 4px rgba(0,0,0,.08);text-align:center;padding-top:24px}
.card svg{width:40px;height:40px}
.card h3{font-size:12.5px;font-weight:500;text-transform:uppercase;margin-top:14px}
.card h3.active{color:var(--blue)}
.card p{font-size:11px;color:var(--muted);line-height:20px;margin:10px auto 0;width:170px;font-weight:300}
.card .btn{margin-top:16px;font-size:7.5px;padding:3px 16px;border-radius:8px}
.testimonial{top:1674px;height:390px;background:linear-gradient(120deg,#2c3138 0%,#48505a 45%,#3a4048 70%,#262a30 100%);color:var(--white);text-align:center}
.quote{position:absolute;top:95px;width:100%;font-size:15px;line-height:22px;font-weight:300}
.quote-by{position:absolute;top:170px;width:100%;font-size:13px;color:var(--blue-bright)}
.play{position:absolute;left:567px;top:309px}
.stats{top:2064px;height:323px;background:var(--slate);color:var(--white)}
.stats .section-title{position:absolute;top:62px;width:100%}
.stat{position:absolute;top:118px;width:260px;text-align:center}
.stat-num{display:flex;justify-content:center;align-items:center;gap:8px;font-size:36px;font-weight:500}
.stat-num small{font-size:22px;margin-left:-6px}
.stat hr{width:66px;border:0;border-top:2px solid var(--white);margin:16px auto 20px}
.stat-label{font-size:11px;text-transform:uppercase}
.team{top:2387px;height:377px;background:var(--light)}
.team .section-title{position:absolute;top:62px;width:100%}
.member{position:absolute;top:110px;width:194px;height:194px;border-radius:50%;border:2px solid var(--blue);overflow:hidden;background:linear-gradient(180deg,#eef0f2 0%,#d8dde2 60%,#c9ced4 100%)}
.member-name{position:absolute;bottom:0;left:0;width:100%;height:42px;background:var(--blue);color:var(--white);font-size:11px;text-transform:uppercase;text-align:center;padding-top:10px}
.site-footer{top:2764px;height:386px;background:var(--footer);color:#c9ccd2}
.col{position:absolute;top:60px;font-size:11px;line-height:21px;font-weight:300}
.col h4{font-size:12.5px;font-weight:600;color:var(--white);text-transform:uppercase;margin-bottom:40px}
.map-btn{display:inline-block;margin-top:20px;background:var(--white);color:var(--ink);font-size:10px;font-weight:600;text-transform:uppercase;width:160px;height:42px;line-height:42px;text-align:center}
.form{position:absolute;left:627px;top:108px;width:480px}
.field{background:var(--field);height:36px;margin-bottom:8px;font-size:10px;color:#8a8e96;padding:10px 12px}
.row{display:flex;gap:8px}
.row .field{flex:1}
.field.tall{height:80px}
.send{width:228px;height:34px;line-height:34px;background:#3b3f48;color:#c9ccd2;font-size:9px;text-align:center;text-transform:uppercase;margin-top:6px}
.bottom-bar{top:3150px;height:82px;background:var(--footer-deep);color:#9a9ea6;font-size:10px}
.social{position:absolute;left:80px;top:36px;display:flex;gap:10px}
.social span{width:10px;height:10px;border-radius:50%;background:#8a8e96}
.copyright{position:absolute;right:80px;top:32px}
</style>
</head>
<body>
<div class="page">
  <section class="hero" role="img" aria-label="Photo of a team around a table with a security planning sketch"></section>
  <header class="site-header">
    <div class="brand"><span class="brand-dot"></span>Tolvane</div>
    <nav class="nav"><span>HOME</span><span>ABOUT US</span><span>OUR SERVICES</span><span>OUR TEAM</span><span>CONTACT US</span></nav>
  </header>

  <section class="about">
    <h2 class="section-title">About Us</h2>
    <p class="about-text">Tolvane is a privately held data security consulting firm that specializes in providing comprehensive information security services for your IT security needs. With a proven track record providing information security services for all industries, Tolvane has aided dozens of organizations worldwide realize and achieve their information security goals. Tolvane offers full consultancy services, as well as implementation of PCI Certification packages and PCI Compliance Consulting to organizations worldwide.</p>
    <span class="btn">Read More</span>
  </section>

  <section class="services">
    <h2 class="section-title">Our Services</h2>
    <div class="card" style="left:80px;top:127px">
      <svg viewBox="0 0 40 40"><circle cx="20" cy="20" r="15" fill="var(--blue)"/><path d="M12 14c4 0 5 3 8 3s2 5-1 6-2 6-5 4-3-7-2-13z" fill="#fff"/></svg>
      <h3>Cyber Security</h3><p>lorem ipsum dolor sit amet, consetetur sadipscing elitr.</p><span class="btn">View Details</span></div>
    <div class="card" style="left:347px;top:127px">
      <svg viewBox="0 0 40 40"><circle cx="15" cy="22" r="9" fill="none" stroke="var(--blue)" stroke-width="5" stroke-dasharray="3 2"/><circle cx="15" cy="22" r="3" fill="var(--blue)"/><circle cx="29" cy="11" r="6" fill="none" stroke="var(--blue)" stroke-width="4" stroke-dasharray="2 2"/></svg>
      <h3>Software Security</h3><p>lorem ipsum dolor sit amet, consetetur sadipscing elitr.</p><span class="btn">View Details</span></div>
    <div class="card" style="left:614px;top:127px">
      <svg viewBox="0 0 40 40"><rect x="11" y="4" width="18" height="32" rx="3" fill="none" stroke="var(--blue)" stroke-width="2.5"/><circle cx="20" cy="31" r="1.6" fill="var(--blue)"/></svg>
      <h3 class="active">Internal Penetration Testing</h3><p>lorem ipsum dolor sit amet, consetetur sadipscing elitr.</p><span class="btn">View Details</span></div>
    <div class="card" style="left:881px;top:127px">
      <svg viewBox="0 0 40 40"><rect x="9" y="5" width="22" height="30" fill="none" stroke="var(--blue)" stroke-width="2.5"/><path d="M14 14h12M14 20h12M14 26h12" stroke="var(--blue)" stroke-width="2"/></svg>
      <h3>External Penetration Testing</h3><p>lorem ipsum dolor sit amet, consetetur sadipscing elitr.</p><span class="btn">View Details</span></div>
    <div class="card" style="left:80px;top:372px">
      <svg viewBox="0 0 40 40"><rect x="5" y="10" width="30" height="21" rx="2" fill="none" stroke="var(--blue)" stroke-width="2.5"/><path d="M5 16h30" stroke="var(--blue)" stroke-width="3"/><path d="M9 25h8" stroke="var(--blue)" stroke-width="2"/></svg>
      <h3>PCI DCI</h3><p>lorem ipsum dolor sit amet, consetetur sadipscing elitr.</p><span class="btn">View Details</span></div>
    <div class="card" style="left:347px;top:372px">
      <svg viewBox="0 0 40 40"><rect x="6" y="8" width="26" height="26" rx="3" fill="none" stroke="var(--blue)" stroke-width="2.5"/><path d="M12 20l6 6 15-17" fill="none" stroke="var(--blue)" stroke-width="3.5"/></svg>
      <h3>ISO 27799</h3><p>lorem ipsum dolor sit amet, consetetur sadipscing elitr.</p><span class="btn">View Details</span></div>
    <div class="card" style="left:614px;top:372px">
      <svg viewBox="0 0 40 40"><path d="M20 4l13 5v10c0 9-6 14-13 17C13 33 7 28 7 19V9z" fill="var(--blue)"/><path d="M20 8v24c5-3 9-7 9-13V11z" fill="#fff"/></svg>
      <h3>Risk Management</h3><p>lorem ipsum dolor sit amet, consetetur sadipscing elitr.</p><span class="btn">View Details</span></div>
    <div class="card" style="left:881px;top:372px">
      <svg viewBox="0 0 40 40"><circle cx="20" cy="12" r="6" fill="var(--blue)"/><path d="M10 34c0-8 4-13 10-13s10 5 10 13z" fill="var(--blue)"/><circle cx="8" cy="17" r="4" fill="var(--blue)"/><circle cx="32" cy="17" r="4" fill="var(--blue)"/><path d="M1 32c0-6 3-9 7-9s5 2 5 2l-3 7zM39 32c0-6-3-9-7-9s-5 2-5 2l3 7z" fill="var(--blue)"/></svg>
      <h3>Professional Services</h3><p>lorem ipsum dolor sit amet, consetetur sadipscing elitr.</p><span class="btn">View Details</span></div>
  </section>

  <section class="testimonial" role="img" aria-label="Dimmed photo of a person working at a laptop in an office">
    <p class="quote">We partner with the world's most innovative<br>security technology companies, and we<br>choose Tolvane Consulting.</p>
    <p class="quote-by">Dana Morrow – CEO, Company Name</p>
    <svg class="play" width="64" height="64" viewBox="0 0 64 64"><circle cx="32" cy="32" r="30" fill="none" stroke="#fff" stroke-width="3"/><path d="M26 20l18 12-18 12z" fill="#fff"/></svg>
  </section>

  <section class="stats">
    <h2 class="section-title">Our Achievements Speaks</h2>
    <div class="stat" style="left:60px">
      <div class="stat-num"><svg width="30" height="30" viewBox="0 0 30 30"><path d="M8 3h14v8a7 7 0 0 1-14 0zM8 6H3c0 5 2 7 5 7M22 6h5c0 5-2 7-5 7M15 18v5M9 27h12" fill="none" stroke="#fff" stroke-width="2.2"/></svg>120</div>
      <hr><div class="stat-label">Completed Projects</div></div>
    <div class="stat" style="left:333px">
      <div class="stat-num"><svg width="30" height="30" viewBox="0 0 30 30"><circle cx="15" cy="11" r="7" fill="none" stroke="#fff" stroke-width="2.2"/><path d="M10 17l-4 10 5-2 3 4 1-6M20 17l4 10-5-2-3 4" fill="none" stroke="#fff" stroke-width="2"/></svg>99<small>%</small></div>
      <hr><div class="stat-label">Satisfied Customers</div></div>
    <div class="stat" style="left:592px">
      <div class="stat-num"><svg width="30" height="30" viewBox="0 0 30 30"><path d="M15 4l12 6-12 6-12-6zM3 15l12 6 12-6M3 20l12 6 12-6" fill="none" stroke="#fff" stroke-width="2.2"/></svg>250</div>
      <hr><div class="stat-label">Verified Certifications</div></div>
    <div class="stat" style="left:872px">
      <div class="stat-num"><svg width="26" height="30" viewBox="0 0 26 30"><path d="M13 3a9 9 0 0 1 5 16v3H8v-3A9 9 0 0 1 13 3zM9 26h8" fill="none" stroke="#fff" stroke-width="2.2"/></svg>2730</div>
      <hr><div class="stat-label">Penetration Tests</div></div>
  </section>

  <section class="team">
    <h2 class="section-title">Our Team</h2>
    <div class="member" style="left:101px" role="img" aria-label="Portrait photo of Noam Keller"><div class="member-name">Noam Keller</div></div>
    <div class="member" style="left:368px" role="img" aria-label="Portrait photo of Eitan Varsh"><div class="member-name">Eitan Varsh</div></div>
    <div class="member" style="left:635px" role="img" aria-label="Portrait photo of Noam Keller"><div class="member-name">Noam Keller</div></div>
    <div class="member" style="left:905px" role="img" aria-label="Portrait photo of Eitan Varsh"><div class="member-name">Eitan Varsh</div></div>
  </section>

  <footer class="site-footer">
    <div class="col" style="left:80px">
      <h4>United States Office</h4>
      418 Harlow Avenue, Suite 1204<br>New York City, NY<br>Zip: 10016 - 2291<br>Office: 1.646.555.0142<br>Mobile: 1.914.555.0178<br>Email: sales@vultrimadvisory.com<br>
      <span class="map-btn">View Map Location</span>
    </div>
    <div class="col" style="left:347px">
      <h4>Israel Office</h4>
      12 Marom Street,<br>Beit Lavan, Ein Tamar<br>Office: 972.8.5550123<br>Mobile 1: 972.52.5550147<br>Mobile 2: 972.54.5550190<br>Email: sales@tolvane.co.il<br>
      <span class="map-btn">View Map Location</span>
    </div>
    <div class="col" style="left:614px"><h4>Send Us A Message</h4></div>
    <div class="form">
      <div class="field">Your Name</div>
      <div class="row"><div class="field">E-Mail</div><div class="field">Subject</div></div>
      <div class="field tall">Message</div>
      <div class="send">Send Message</div>
    </div>
  </footer>

  <footer class="bottom-bar">
    <div class="social"><span></span><span></span><span></span><span></span></div>
    <div class="copyright">© Copyright Tolvane, 2016. All Rights Reserved</div>
  </footer>
</div>
</body>
</html>
```